Simple templates for management consulting firm

Vireo Advisors is a management consulting firm based in the DC area. We have all the basic templates but would like to tweak them so they look consistent.

Check us out at www.vireoadvisors-example.com

For this project we would like to get
a tweaked powerpoint template (header should be up)
a letter template for letters
a fax template

Current templates and our logo are attached.
Updates

We just increased the budget of this project.

We got questions about the project. Here are our thoughts on this one:

Please include the logo into the fax template. If you find improvements in the layout then feel free to make those. Let's not overthink this too much. Keep it simple :)

We like The powerpoint concept as is. The slide titles are for some reasons on the bottom. It seems to irritate some folks. If you can switch the slide titles to the top, keep the look and feel of the slides and work in the logo then that would be fantastic.

The letter head should include the following

Vireo Advisors, LLC Box 5817, Pine Hollow, VA 20499 Phone 555 814-2906, Fax 555 276 9143, www.vireoadvisors-example.com and the logo.

Again, let's keep it simple.

Thank you for considering this project.

We just realize that we are not necessarily inisting to use the red in the slides.
Any approach that would work with the logo will be considered.

Thanks for your creativity.

Target Market(s)

tech companies, Meridian 400, venture capitalists

Industry/Entity Type

Management Consulting

Requirements
Must have
• Keep it simple please

```html
<!DOCTYPE html>
<html lang="en">
<head>
<meta charset="utf-8">
<title>Vireo Advisors – Slide Template</title>
<link href="https://fonts.googleapis.com/css2?family=Tinos:wght@400&display=swap" rel="stylesheet">
<style>
  :root {
    --stage: #d4d4d4;
    --paper: #ffffff;
    --ink: #1e1e1e;
    --gold: #c9a43c;
    --band: #717171;
    --mark-grey: #8a8a8a;
  }
  * { box-sizing: border-box; margin: 0; padding: 0; }
  html, body { width: 1200px; height: 923px; overflow: hidden; }
  body {
    background: var(--stage);
    font-family: "Tinos", "Times New Roman", serif;
    color: var(--ink);
    position: relative;
  }
  .slide {
    position: absolute;
    width: 545px;
    height: 422px;
    background: var(--paper);
    box-shadow: 0 1px 4px rgba(0,0,0,0.35);
    overflow: hidden;
  }
  .slide--title { left: 33px; top: 260px; }
  .slide--agenda { left: 622px; top: 20px; width: 546px; height: 421px; }
  .slide--content { left: 617px; top: 471px; }

  /* footer band */
  .footer {
    position: absolute;
    left: 0; right: 0; bottom: 0;
    height: 30px;
    background: var(--band);
  }
  .footer svg { position: absolute; left: 0; top: 0; }
  .footer__legal {
    position: absolute;
    left: 65px; right: 20px; top: 8px;
    font-size: 6.3px;
    line-height: 7.4px;
    color: #fff;
  }

  /* brand mark */
  .brand { display: flex; align-items: center; gap: 8px; }
  .brand__dot { border-radius: 50%; background: var(--gold); flex: none; }
  .brand__name { color: var(--mark-grey); white-space: nowrap; }

  .brand--large {
    position: absolute; left: 143px; top: 62px;
  }
  .brand--large .brand__dot { width: 78px; height: 78px; }
  .brand--large .brand__name { font-size: 34px; }

  .brand--small {
    position: absolute; right: 20px; top: 20px;
    gap: 5px;
  }
  .brand--small .brand__dot { width: 30px; height: 30px; }
  .brand--small .brand__name { font-size: 15px; }

  .header-rule {
    position: absolute;
    right: 0; top: 62px;
    width: 124px; height: 3px;
    background: var(--gold);
  }

  /* title slide */
  .presenter {
    position: absolute;
    left: 0; right: 0; top: 222px;
    text-align: center;
    font-size: 28px;
    line-height: 41px;
  }

  /* agenda slide */
  .agenda__heading {
    position: absolute; left: 38px; top: 18px;
    font-size: 38px; font-weight: 400;
  }
  .agenda__list {
    position: absolute; left: 38px; top: 110px;
    list-style: none;
    font-size: 23.5px;
    line-height: 32px;
  }
  .agenda__list li::before {
    content: "•";
    color: var(--gold);
    display: inline-block;
    width: 14px;
    font-size: 20px;
  }

  /* content slide */
  .content__heading {
    position: absolute; left: 37px; top: 20px;
    font-size: 23px; font-weight: 400;
    letter-spacing: 0.6px;
  }
  .content__body {
    position: absolute; left: 36px; top: 100px; width: 480px;
    font-size: 18px;
    line-height: 24.5px;
  }
  .content__body p + p { margin-top: 24.5px; }
  .accent { color: var(--gold); }
</style>
</head>
<body>

  <section class="slide slide--title">
    <div class="brand brand--large">
      <span class="brand__dot"></span>
      <span class="brand__name">Vireo Advisors</span>
    </div>
    <p class="presenter">Daniel Harrow<br>Managing Partner</p>
    <footer class="footer">
      <svg width="70" height="30" viewBox="0 0 70 30">
        <polygon points="0,0 30,0 36,30 0,30" fill="var(--gold)"/>
        <polygon points="30,0 36,0 42,30 36,30" fill="#fff"/>
      </svg>
      <p class="footer__legal">Copyright © 2012 by Vireo Advisors, LLC. All rights reserved. This document contains confidential and proprietary information and may not be reproduced, in whole or in part, without express written permission from Vireo Advisors, LLC.</p>
    </footer>
  </section>

  <section class="slide slide--agenda">
    <h1 class="agenda__heading">AGENDA</h1>
    <div class="brand brand--small">
      <span class="brand__dot"></span>
      <span class="brand__name">Vireo Advisors</span>
    </div>
    <div class="header-rule"></div>
    <ul class="agenda__list">
      <li>Jumpstart Your Business</li>
      <li>Mastering the Sale</li>
      <li>Getting Projects Done</li>
      <li>Turnaround</li>
      <li>Vireo Advisor’s Engagement Model</li>
      <li>About Tobias Lindqvist</li>
    </ul>
    <footer class="footer">
      <svg width="70" height="30" viewBox="0 0 70 30">
        <polygon points="0,0 30,0 36,30 0,30" fill="var(--gold)"/>
        <polygon points="30,0 36,0 42,30 36,30" fill="#fff"/>
      </svg>
      <p class="footer__legal">Copyright © 2012 by Vireo Advisors, LLC. All rights reserved. This document contains confidential and proprietary information and may not be reproduced, in whole or in part, without express written permission from Vireo Advisors, LLC.</p>
    </footer>
  </section>

  <section class="slide slide--content">
    <h1 class="content__heading">JUMPSTART YOUR BUSINESS</h1>
    <div class="brand brand--small">
      <span class="brand__dot"></span>
      <span class="brand__name">Vireo Advisors</span>
    </div>
    <div class="header-rule"></div>
    <div class="content__body">
      <p>In its essence, business is about <span class="accent">Sales</span> and <span class="accent">Projects</span>. Most things a company does fall in these two categories. Vireo Advisors helps your company to <span class="accent">grow revenue</span>. We help you to maintain <span class="accent">a handle on the important projects</span>. We help you to <span class="accent">turnaround</span> your organization.</p>
      <p>Most importantly, we do it <span class="accent">quickly</span>.</p>
    </div>
    <footer class="footer">
      <svg width="70" height="30" viewBox="0 0 70 30">
        <polygon points="0,0 30,0 36,30 0,30" fill="var(--gold)"/>
        <polygon points="30,0 36,0 42,30 36,30" fill="#fff"/>
      </svg>
      <p class="footer__legal">Copyright © 2012 by Vireo Advisors, LLC. All rights reserved. This document contains confidential and proprietary information and may not be reproduced, in whole or in part, without express written permission from Vireo Advisors, LLC.</p>
    </footer>
  </section>

</body>
</html>
```